Corvelle Strategies business card

I need a business card for my new strategic consulting LLC, Corvelle Strategies. We specialize in helping people who care about broadband technology and telecommunications policy, and we're based in Washington DC. I'm looking for a card that says smart, credible, future-facing and signals a high level of expertise. It's DC, so there's clearly a limit to how crazy we can go with this card, but I am looking for a design that reflects a company that is comfortable with technology, policy, and having a little bit fun. I'm uploading my logo below, and I'd like to have it be part of the card design in some fashion.
Target Market(s)
Telecommunications and technology policy professionals
Industry/Entity Type
Technology policy
Contact Information for Business Card
Name of business, my name (Glen Mosswater), email (glen@corvellestrategies-example.com) , phone number (202-555-0148)phone number

```html
<!DOCTYPE html>
<html lang="en">
<head>
<meta charset="utf-8">
<title>Corvelle Strategies business card</title>
<link rel="stylesheet" href="https://fonts.googleapis.com/css2?family=Montserrat:wght@400;700&display=swap">
<style>
  :root {
    --backdrop: #d3d8d8;
    --paper: #f1f1ef;
    --brand-blue: #0a4fa3;
    --sun-orange: #f6ac3b;
    --ink-grey: #3a3d42;
  }
  * { margin: 0; padding: 0; box-sizing: border-box; }
  html, body { width: 1200px; height: 881px; overflow: hidden; }
  body {
    background: var(--backdrop);
    font-family: "Montserrat", Arial, sans-serif;
    display: flex;
    align-items: center;
    justify-content: center;
    gap: 60px;
  }
  .card {
    position: relative;
    width: 525px;
    height: 300px;
    background: var(--paper);
    border-bottom: 5px solid var(--brand-blue);
    border-right: 2px solid var(--brand-blue);
    box-shadow: 0 14px 30px rgba(0,0,0,0.18);
  }
  .wordmark {
    color: var(--brand-blue);
    font-weight: 700;
    line-height: 1;
    display: flex;
    align-items: center;
    gap: 10px;
  }
  .wordmark-dot {
    border-radius: 50%;
    background: var(--sun-orange);
    flex: none;
  }
  /* contact side */
  .card-contact .wordmark {
    position: absolute;
    top: 34px;
    left: 34px;
    font-size: 26px;
  }
  .card-contact .wordmark-dot { width: 16px; height: 16px; }
  .accent-line {
    position: absolute;
    left: 0;
    top: 196px;
    width: 200px;
    height: 2px;
    background: var(--brand-blue);
  }
  .accent-dot {
    position: absolute;
    left: 212px;
    top: 184px;
    width: 24px;
    height: 24px;
    border-radius: 50%;
    background: var(--sun-orange);
  }
  .holder {
    position: absolute;
    left: 260px;
    top: 158px;
    right: 24px;
  }
  .holder-name {
    color: var(--brand-blue);
    font-weight: 700;
    font-size: 23px;
    padding-bottom: 8px;
    border-bottom: 2px solid var(--brand-blue);
  }
  .contact-list {
    list-style: none;
    margin-top: 10px;
    color: var(--ink-grey);
    font-size: 12.5px;
  }
  .contact-list li {
    display: flex;
    align-items: center;
    gap: 8px;
    margin-bottom: 6px;
  }
  .contact-list svg { width: 11px; height: 11px; fill: var(--brand-blue); flex: none; }
  /* brand side */
  .card-brand {
    display: flex;
    align-items: center;
    justify-content: center;
  }
  .card-brand .wordmark { font-size: 40px; }
  .card-brand .wordmark-dot { width: 26px; height: 26px; }
</style>
</head>
<body>
  <section class="card card-contact">
    <div class="wordmark"><span>Corvelle Strategies</span><span class="wordmark-dot"></span></div>
    <div class="accent-line"></div>
    <div class="accent-dot"></div>
    <div class="holder">
      <p class="holder-name">Glen Mosswater</p>
      <ul class="contact-list">
        <li>
          <svg viewBox="0 0 24 24" aria-hidden="true"><path d="M6.6 10.8a15.1 15.1 0 0 0 6.6 6.6l2.2-2.2a1 1 0 0 1 1-.25 11.4 11.4 0 0 0 3.6.57 1 1 0 0 1 1 1V20a1 1 0 0 1-1 1A17 17 0 0 1 3 4a1 1 0 0 1 1-1h3.5a1 1 0 0 1 1 1c0 1.25.2 2.45.57 3.6a1 1 0 0 1-.25 1z"/></svg>
          202-555-0148
        </li>
        <li>
          <svg viewBox="0 0 24 24" aria-hidden="true"><path d="M2 5h20v14H2z M2 5l10 8 10-8" /></svg>
          corvellestrategies-example.com
        </li>
      </ul>
    </div>
  </section>

  <section class="card card-brand">
    <div class="wordmark"><span>Corvelle Strategies</span><span class="wordmark-dot"></span></div>
  </section>
</body>
</html>
```